Whitmore Business Card Design

The name of the business is Dara Whitmore, CPA LLC
The service that we offer is Accounting, Tax & Consulting Services. I need it to have the following items:
Dara Whitmore, Principal
Phone Number
Email Address
Physical Address

I have attached the company logo, one in black and one in white. Please provide a design in black background and the other in white background. Please include "Accounting, Tax & Consulting Services". I want the business card to be clean and very professional.

```html
<!DOCTYPE html>
<html lang="en">
<head>
<meta charset="utf-8">
<title>Dara Whitmore, CPA LLC — Business Card</title>
<link rel="stylesheet" href="https://fonts.googleapis.com/css2?family=Montserrat:wght@400;500;600;700&display=swap">
<style>
  :root {
    --page-bg: #161616;
    --card-bg: #1f1f20;
    --card-edge: #2a2a2b;
    --brand-red: #9a1c1f;
    --brand-grey: #6e6e70;
    --text-light: #f2f2f2;
    --text-muted: #8d8d8f;
  }
  * { box-sizing: border-box; margin: 0; padding: 0; }
  html, body {
    width: 1200px; height: 988px; overflow: hidden;
    background: var(--page-bg);
    font-family: "Montserrat", sans-serif;
  }
  .canvas {
    width: 1200px; height: 988px;
    display: flex; flex-direction: column; align-items: center; justify-content: center;
    gap: 48px;
  }
  .card {
    position: relative;
    width: 700px; height: 400px;
    background: var(--card-bg);
    border: 1px solid var(--card-edge);
    box-shadow: 0 18px 40px rgba(0,0,0,.55);
    overflow: hidden;
  }

  /* Brand lockup */
  .brand { display: flex; align-items: center; gap: 18px; }
  .brand-mark { width: 22px; height: 22px; background: var(--brand-red); flex: none; }
  .brand-text { display: flex; flex-direction: column; }
  .brand-name {
    color: var(--brand-grey); font-weight: 500; text-transform: uppercase;
    letter-spacing: 1px; line-height: 1;
  }
  .brand-tagline {
    color: var(--text-muted); font-weight: 500; text-transform: uppercase;
    letter-spacing: 3px; margin-top: 8px;
  }

  /* Front */
  .card--front .brand { position: absolute; left: 150px; top: 140px; }
  .card--front .brand-mark { width: 30px; height: 30px; }
  .card--front .brand-name { font-size: 30px; }
  .card--front .brand-tagline { font-size: 19px; }
  .card--front .services {
    color: var(--text-muted); font-weight: 700; font-size: 17px; margin-top: 16px;
  }

  /* Back */
  .card--back .brand { position: absolute; left: 70px; top: 238px; }
  .card--back .brand-mark { width: 18px; height: 18px; }
  .card--back .brand-name { font-size: 17px; }
  .card--back .brand-tagline { font-size: 10px; letter-spacing: 2.4px; margin-top: 5px; }

  .name-band {
    position: absolute; left: 360px; right: 0; top: 70px; height: 56px;
    background: var(--brand-red);
    display: flex; align-items: center; padding-left: 26px;
    color: #fff; font-weight: 700; font-size: 20px; text-transform: uppercase;
  }
  .contact-list {
    position: absolute; left: 388px; top: 150px;
    list-style: none; display: flex; flex-direction: column; gap: 16px;
  }
  .contact-item { display: flex; align-items: center; gap: 14px; color: var(--text-light); font-size: 15px; line-height: 1.35; }
  .contact-icon {
    width: 26px; height: 26px; border-radius: 50%; background: var(--brand-red);
    display: flex; align-items: center; justify-content: center; flex: none;
  }
  .contact-icon svg { width: 14px; height: 14px; fill: #fff; }
</style>
</head>
<body>
<main class="canvas">

  <section class="card card--front">
    <div class="brand">
      <span class="brand-mark"></span>
      <div class="brand-text">
        <span class="brand-name">Dara Whitmore, CPA LLC</span>
        <span class="brand-tagline">Certified Public Accountant</span>
        <span class="services">Accounting, Tax &amp; Consulting Services</span>
      </div>
    </div>
  </section>

  <section class="card card--back">
    <div class="brand">
      <span class="brand-mark"></span>
      <div class="brand-text">
        <span class="brand-name">Dara Whitmore, CPA LLC</span>
        <span class="brand-tagline">Certified Public Accountant</span>
      </div>
    </div>

    <div class="name-band">Dara Whitmore, Principal</div>

    <ul class="contact-list">
      <li class="contact-item">
        <span class="contact-icon"><svg viewBox="0 0 24 24"><path d="M12 2a7 7 0 0 0-7 7c0 5 7 13 7 13s7-8 7-13a7 7 0 0 0-7-7zm0 9.5A2.5 2.5 0 1 1 12 6.5a2.5 2.5 0 0 1 0 5z"/></svg></span>
        <span>#208-C, Lakeview Court,<br>Harbor Road, Millbrook, 402117</span>
      </li>
      <li class="contact-item">
        <span class="contact-icon"><svg viewBox="0 0 24 24"><path d="M6.6 10.8a15 15 0 0 0 6.6 6.6l2.2-2.2a1 1 0 0 1 1-.25 11.4 11.4 0 0 0 3.6.57 1 1 0 0 1 1 1V20a1 1 0 0 1-1 1A17 17 0 0 1 3 4a1 1 0 0 1 1-1h3.5a1 1 0 0 1 1 1c0 1.25.2 2.45.57 3.6a1 1 0 0 1-.25 1z"/></svg></span>
        <span>555-214-7390</span>
      </li>
      <li class="contact-item">
        <span class="contact-icon"><svg viewBox="0 0 24 24"><path d="M2 5h20v14H2zm2 2v.5l8 5 8-5V7l-8 5z"/></svg></span>
        <span>info@darawhitmorecpallc.com</span>
      </li>
      <li class="contact-item">
        <span class="contact-icon"><svg viewBox="0 0 24 24"><path d="M12 2a10 10 0 1 0 0 20 10 10 0 0 0 0-20zm6.9 6h-3a15.6 15.6 0 0 0-1.4-3.6A8 8 0 0 1 18.9 8zM12 4a14 14 0 0 1 1.9 4h-3.8A14 14 0 0 1 12 4zM4.3 14a8 8 0 0 1 0-4h3.4a16 16 0 0 0 0 4zm.8 2h3a15.6 15.6 0 0 0 1.4 3.6A8 8 0 0 1 5.1 16zm3-8h-3a8 8 0 0 1 4.4-3.6A15.6 15.6 0 0 0 8.1 8zM12 20a14 14 0 0 1-1.9-4h3.8A14 14 0 0 1 12 20zm2.3-6H9.7a14 14 0 0 1 0-4h4.6a14 14 0 0 1 0 4zm.2 5.6a15.6 15.6 0 0 0 1.4-3.6h3a8 8 0 0 1-4.4 3.6zm1.8-5.6a16 16 0 0 0 0-4h3.4a8 8 0 0 1 0 4z"/></svg></span>
        <span>www.darawhitmorecpallc.com</span>
      </li>
    </ul>
  </section>

</main>
</body>
</html>
```